つい手に取ってなんだろう?って思うくらいのインパクトのあるラベルデザインを求めます。鬼をイメージしたデザイン希望ですが、昔から全国各地に「霞まくら」という日本酒が多数存在するため、それらとイメージが被らない印象が良いです。
1.8L(一升瓶)のラベルです。基本的には140×140の正方形のラベル印刷を予定していますがその枠内であれば形状、サイズフリーでも大丈夫です。
過去使用したロゴデータを追記しました。使用してもしなくても構いません。

おもわず手に取ってしまうようなインパクトのある印象的なラベルでしたのでこの提案を選びました。

たくさんのご提案ありがとうございます。
素晴らしいデザインが多く検討に時間を要しました。
また何かありましたら今後ともよろしくお願いいたします。

```html
<!DOCTYPE html>
<html lang="ja">
<head>
<meta charset="utf-8">
<title>澄心静水 鬼辛純米 ラベル</title>
<link href="https://fonts.googleapis.com/css2?family=Yuji+Boku&family=Noto+Serif+JP:wght@700&family=Noto+Serif:ital@1&display=swap" rel="stylesheet">
<style>
  :root {
    --canvas: #ffffff;
    --ink: #ffffff;
    --oni-ink: 12, 10, 10;
    --green-light: #6a866a;
    --green-mid: #3f5c45;
    --green-dark: #24382a;
    --red-light: #c8181f;
    --red-mid: #8c1015;
    --red-dark: #4c0709;
  }
  * { box-sizing: border-box; margin: 0; padding: 0; }
  html, body {
    width: 678px; height: 1200px; overflow: hidden;
    background: var(--canvas);
  }
  .label {
    position: absolute;
    left: 154px;
    width: 370px; height: 370px;
    overflow: hidden;
    color: var(--ink);
  }
  .label--green {
    top: 153px;
    background: linear-gradient(135deg, var(--green-light) 0%, var(--green-mid) 55%, var(--green-dark) 100%);
  }
  .label--red {
    top: 654px;
    background: linear-gradient(135deg, var(--red-light) 0%, var(--red-mid) 55%, var(--red-dark) 100%);
  }
  .oni-mark {
    position: absolute;
    left: 0; top: 0;
    width: 370px; height: 370px;
    background:
      radial-gradient(ellipse 130px 170px at 110px 210px, rgba(var(--oni-ink),0.92) 0%, rgba(var(--oni-ink),0.8) 55%, rgba(var(--oni-ink),0) 100%),
      radial-gradient(ellipse 90px 60px at 230px 330px, rgba(var(--oni-ink),0.75) 0%, rgba(var(--oni-ink),0) 100%),
      radial-gradient(ellipse 70px 90px at 250px 150px, rgba(var(--oni-ink),0.6) 0%, rgba(var(--oni-ink),0) 100%);
  }
  .limited {
    position: absolute;
    left: 14px; top: 92px;
    width: 42px; height: 236px;
    border-top: 3px solid var(--ink);
    border-bottom: 3px solid var(--ink);
    display: flex; justify-content: center; align-items: center;
    writing-mode: vertical-rl;
    font-family: "Noto Serif JP", serif;
    font-weight: 700;
    font-size: 29px;
    line-height: 1;
    letter-spacing: 2px;
  }
  .product-name {
    position: absolute;
    left: 80px; top: 52px;
    writing-mode: vertical-rl;
    font-family: "Yuji Boku", serif;
    font-size: 70px;
    line-height: 1;
  }
  .style-name {
    position: absolute;
    left: 256px; top: 36px;
    writing-mode: vertical-rl;
    font-family: "Yuji Boku", serif;
    font-size: 52px;
    line-height: 1;
  }
  .volume {
    position: absolute;
    left: 12px; top: 334px;
    font-family: "Noto Serif", serif;
    font-size: 19px;
    line-height: 1;
  }
  .tagline {
    position: absolute;
    left: 250px; top: 268px;
    width: 108px;
    font-family: "Noto Serif", serif;
    font-style: italic;
    font-size: 6.5px;
    line-height: 1.4;
  }
</style>
</head>
<body>
  <section class="label label--green">
    <div class="oni-mark" role="img" aria-label="大きな筆書きの鬼の文字"></div>
    <div class="limited">専門酒販店限定</div>
    <div class="product-name">澄心静水</div>
    <div class="style-name">鬼辛純米</div>
    <div class="volume">1.8L</div>
    <p class="tagline">A crisp junmai sake with honest rice flavour, brewed dry and bold for every table and season.</p>
  </section>

  <section class="label label--red">
    <div class="oni-mark" role="img" aria-label="大きな筆書きの鬼の文字"></div>
    <div class="limited">専門酒販店限定</div>
    <div class="product-name">澄心静水</div>
    <div class="style-name">鬼辛純米</div>
    <div class="volume">1.8L</div>
    <p class="tagline">A crisp junmai sake with honest rice flavour, brewed dry and bold for every table and season.</p>
  </section>
</body>
</html>
```